Commercial Cleaning Company Website Design

We are working with Harbor Tidy Squad. They are a commercial cleaning company that needs a new website design.

Some sites to use for inspiration:

https://www.velmoxa.com
https://glint-panewashing.com
https://tidykelps.net
https://warmnestdwell.com
https://www.thescrubbingcouncil.com
https://www.pennybroom.com

Thank you for taking the time to consider designing a website for us. We are web developers based in Stockton and Los Angeles, CA, USA. Most of our projects go through the same process. Understanding this process may help you win a project with us. We custom-code all of our websites in-house. We don’t have any requirements as to what tools you use for your design, but we prefer Figma files. For any design that we label as four-stars, we send it to the client for review. The client picks the final design they want us to use. Once we complete this process, we will continue to show additional clients all the four-star sites and purchase them later. Your designs will have multiple chances to sell. For better chances of success, we ask that you follow these guidelines.

IMAGES:
If you use any images or icons in the design, we ask that you have a link to the asset so we can purchase the image/icon. Most of the designs we submit do not have the customer’s images on them unless they have some great images. Be creative; show us the feeling you are trying to portray with your image choices. Use any royalty-free site you choose. We subscribe to Vorlan and mainly use their images, but we can purchase images outside of Vorlan.

PLEASE NOTE: we will not submit designs to clients with watermarks on the images.

FONTS:
We ask that you identify the fonts used in the design. This can be done in a message if you want. We typically use Google Fonts and Vorlan Fonts.

CONTENT:
We're always open to different content and ideas. We often submit designs with stock images so the client can see our vision. We typically take pictures after the website launch to use their images with our vision. Lorem Ipsum is fine for paragraphs, but we ask that you write the headers in correct English. We want to be able to show the vision and identify the sections of the website.

INSPIRATION:
We typically add a couple of links in the brief of websites we like to help you get started in your design.

REVISIONS:
We do not often ask for revisions of the designs unless we see something in the design that may not appeal to the client. If there are slight changes that we want to make, we do that in the development process.

FEEDBACK:
We rarely give feedback on designs during the design process. We are working on many website projects and do not have the time to provide feedback. We usually respond if your request is well thought out and asks specific questions, but a note asking “feedback, please” usually goes unanswered.

```html
<!DOCTYPE html>
<html lang="en">
<head>
<meta charset="utf-8">
<title>Harbor Tidy Squad — Commercial Cleaning</title>
<link rel="stylesheet" href="https://fonts.googleapis.com/css2?family=Poppins:wght@300;400;500;600;700;800&display=swap">
<style>
:root{
  --blue:#1e4fb8;
  --blue-dark:#173f96;
  --orange:#f7941d;
  --orange-deep:#f05a22;
  --yellow:#ffc629;
  --red:#e8342a;
  --ink:#222;
  --muted:#555;
  --ghost:#eef0f4;
  --white:#fff;
  --line:#d9d9d9;
  --grad:linear-gradient(90deg,var(--yellow),var(--orange) 45%,var(--red));
}
*{box-sizing:border-box;margin:0;padding:0}
html,body{width:1200px;height:5076px;overflow:hidden}
body{font-family:"Poppins",sans-serif;color:var(--ink);background:var(--white);position:relative}
.abs{position:absolute}
.btn{position:absolute;display:flex;align-items:center;justify-content:center;border-radius:40px;font-weight:600;font-size:17px;letter-spacing:.5px;text-transform:uppercase}
.btn-grad{background:var(--grad);color:var(--white)}
.btn-outline{background:var(--white);border:2px solid var(--orange);color:var(--ink)}
.btn-grey{background:#6b6b6b;color:var(--white);font-size:13px}
.photo{position:absolute}

/* header */
.brand{left:40px;top:34px;display:flex;align-items:center;gap:14px}
.brand-dot{width:44px;height:44px;border-radius:50%;background:var(--orange)}
.brand-name{font-size:30px;font-weight:700;color:var(--blue);letter-spacing:2px;line-height:1.05;text-transform:uppercase}
.top-cta{left:724px;top:18px;width:230px;height:40px;font-size:14px;border-width:2px;border-color:var(--red)}
.top-phone{left:972px;top:18px;width:160px;height:40px;font-size:14px;gap:8px;justify-content:flex-start;padding-left:6px}
.phone-ico{width:30px;height:30px;border-radius:50%;background:var(--white);display:flex;align-items:center;justify-content:center}
.nav{left:578px;top:82px;display:flex;gap:36px;font-size:15px;font-weight:500;text-transform:uppercase}
.nav .active{color:var(--red)}

/* hero */
.hero{left:0;top:140px;width:1200px;height:694px;background:linear-gradient(120deg,#8a6a48,#c9a47a 35%,#e6dccf 60%,#a88e70)}
.hero-panel{left:80px;top:232px;width:640px;height:510px;background:rgba(255,255,255,.28);border-radius:22px}
.hero-title{left:130px;top:330px;font-weight:700;font-size:66px;line-height:1.04;text-transform:uppercase}
.hero-title .w{color:var(--white)}
.hero-title .b{color:var(--blue)}
.hero-copy{left:130px;top:490px;width:560px;font-size:16px;color:var(--white);line-height:1.5}
.hero-book{left:186px;top:562px;width:230px;height:60px}
.hero-call{left:400px;top:562px;width:210px;height:60px;font-size:16px}

/* features */
.feature{top:912px;height:76px;width:256px;background:var(--white);border-radius:10px;box-shadow:0 4px 18px rgba(0,0,0,.14);display:flex;align-items:center;gap:12px;padding:0 16px}
.feature-ico{flex:none;width:44px;height:44px;border-radius:50%;background:var(--grad);display:flex;align-items:center;justify-content:center}
.feature h4{font-size:13px;font-weight:700;text-transform:uppercase}
.feature p{font-size:11px;color:var(--muted)}

/* section titles */
.ghost{font-weight:800;color:var(--ghost);font-size:140px;letter-spacing:4px;text-transform:uppercase;line-height:1}
.section-title{font-weight:700;color:var(--blue);font-size:58px;text-transform:uppercase;line-height:1}

/* about */
.about-lead{left:108px;top:1288px;width:500px;font-size:20px;font-weight:700;line-height:1.3;color:#111}
.about-copy{left:108px;top:1380px;width:500px;font-size:15px;line-height:1.7;color:var(--muted)}
.about-btn{left:108px;top:1560px;width:152px;height:52px;font-size:13px}
.about-photo{left:632px;top:1120px;width:464px;height:536px;background:linear-gradient(160deg,#cfc9bf,#7c7b78 55%,#3e3e3e);border-radius:8px}
.about-frame{left:654px;top:1146px;width:420px;height:484px;border:2px solid rgba(255,255,255,.85)}

/* services */
.card{top:1992px;height:466px;background:var(--white);box-shadow:0 4px 20px rgba(0,0,0,.14)}
.card .photo{left:14px;top:14px;right:14px;height:232px}
.card h3{position:absolute;top:270px;left:0;right:0;text-align:center;color:var(--red);font-size:19px;font-weight:600;text-transform:uppercase}
.card p{position:absolute;top:304px;left:24px;right:24px;text-align:center;font-size:14px;line-height:1.55;color:var(--muted)}
.card .btn{left:50%;transform:translateX(-50%);top:396px;width:112px;height:40px}
.services-btn{left:500px;top:2524px;width:200px;height:56px;font-size:13px}

/* welcome band */
.welcome{left:0;top:2688px;width:1200px;height:536px;background:var(--grad)}
.welcome-circle{left:530px;top:2688px;width:670px;height:536px;border-radius:268px 0 0 268px;background:rgba(255,255,255,.22)}
.welcome-photo{left:556px;top:2700px;width:644px;height:524px;border-radius:262px 0 0 262px;background:linear-gradient(135deg,#d8d1c7,#8d8378 55%,#3d3a38)}
.welcome-kicker{left:72px;top:2850px;color:var(--white);font-size:16px;font-weight:500;text-transform:uppercase}
.welcome-title{left:70px;top:2882px;color:var(--white);font-size:68px;font-weight:500;line-height:1;text-transform:uppercase}
.welcome-copy{left:72px;top:3100px;width:440px;color:var(--white);font-size:14px;line-height:1.5}
.welcome-btn{left:72px;top:3162px;width:160px;height:44px;background:var(--white);color:var(--ink);font-size:13px}

/* testimonials */
.quote-mark{left:552px;top:3560px}
.quote-text{left:250px;top:3672px;width:700px;text-align:center;font-size:17px;font-style:italic;line-height:1.6}
.quote-name{left:0;width:1200px;top:3798px;text-align:center;color:var(--blue);font-weight:600;font-size:18px;text-transform:uppercase}
.stars{left:0;width:1200px;top:3830px;display:flex;justify-content:center;gap:4px}
.arrow{top:3690px;width:44px;height:44px;border-radius:50%;background:#ccc;display:flex;align-items:center;justify-content:center}

/* contact */
.contact-intro{left:70px;top:4100px;font-size:15px;color:var(--muted)}
.field{position:absolute;height:54px;border:1px solid var(--line);background:var(--white);box-shadow:0 2px 8px rgba(0,0,0,.08);font-size:13px;color:#999;padding:18px 14px}
.contact-btn{left:70px;top:4460px;width:190px;height:44px;font-size:12px}
.contact-photo{left:720px;top:4020px;width:296px;height:460px;background:linear-gradient(160deg,#c6c0b8,#5b5855 55%,#232323);border-radius:6px}

/* footer */
.footer{left:0;top:4600px;width:1200px;height:476px;background:linear-gradient(100deg,var(--yellow),var(--orange) 50%,var(--red))}
.foot-brand{left:150px;top:4730px;display:flex;align-items:center;gap:14px}
.foot-brand .brand-name{color:var(--white);font-size:36px}
.foot-brand .brand-dot{background:var(--white)}
.socials{left:210px;top:4838px;display:flex;gap:12px}
.socials span{width:36px;height:36px;border-radius:50%;background:var(--white)}
.foot-head{color:var(--white);font-weight:600;font-size:28px;text-transform:uppercase}
.foot-links{left:550px;top:4770px;list-style:none;color:var(--white);font-size:15px;line-height:2.1}
.foot-links li::before{content:"";display:inline-block;width:6px;height:6px;border-radius:50%;background:var(--white);margin-right:12px;vertical-align:middle}
.foot-contact{left:820px;color:var(--white);font-size:15px;display:flex;gap:14px;align-items:center;width:300px;line-height:1.35}
.foot-contact .ic{flex:none;width:34px;height:34px;border-radius:50%;background:var(--white);display:flex;align-items:center;justify-content:center}
.copyright{left:0;width:1200px;top:5030px;text-align:center;color:var(--white);font-size:14px}
</style>
</head>
<body>

<!-- Header -->
<div class="abs brand"><span class="brand-dot"></span><span class="brand-name">Harbor Tidy<br>Squad</span></div>
<div class="btn btn-outline top-cta">Get Your Free Estimate</div>
<div class="btn btn-grad top-phone"><span class="phone-ico"><svg width="16" height="16" viewBox="0 0 24 24"><path fill="#f05a22" d="M6.6 10.8a15 15 0 0 0 6.6 6.6l2.2-2.2c.3-.3.7-.4 1-.2 1.1.4 2.3.6 3.6.6.6 0 1 .4 1 1V20c0 .6-.4 1-1 1A17 17 0 0 1 3 4c0-.6.4-1 1-1h3.5c.6 0 1 .4 1 1 0 1.3.2 2.5.6 3.6.1.3 0 .7-.2 1z"/></svg></span>555-014-2290</div>
<nav class="abs nav"><span class="active">Home</span><span>About Us</span><span>Our Services</span><span>Our Testimonials</span><span>Contact Us</span></nav>

<!-- Hero -->
<div class="photo hero" role="img" aria-label="Gloved hand cleaning a table in a bright office"></div>
<div class="abs hero-panel"></div>
<h1 class="abs hero-title"><span class="w">Professional</span><br><span class="b">Cleaning Services</span></h1>
<p class="abs hero-copy">Lorem ipsum dolor sit amet, consectetur adipiscing elit, sed do eiusmod tempor incididunt ut labore et dolore magna aliqua.</p>
<div class="btn btn-grad hero-book">Book Now</div>
<div class="btn btn-outline hero-call">Call Us Today</div>

<!-- Features -->
<div class="abs feature" style="left:72px"><span class="feature-ico"><svg width="22" height="22" viewBox="0 0 24 24"><circle cx="9" cy="8" r="3.5" fill="#fff"/><path d="M2 20c0-4 3-6 7-6s7 2 7 6z" fill="#fff"/><circle cx="17" cy="9" r="2.5" fill="#fff"/></svg></span><div><h4>Professional Team</h4><p>Lorem ipsum dolor sit amet.</p></div></div>
<div class="abs feature" style="left:346px"><span class="feature-ico"><svg width="22" height="22" viewBox="0 0 24 24"><circle cx="12" cy="12" r="9" fill="none" stroke="#fff" stroke-width="2"/><path d="M12 7v5l3 3" stroke="#fff" stroke-width="2" fill="none"/></svg></span><div><h4>On Time Service</h4><p>Lorem ipsum dolor sit amet.</p></div></div>
<div class="abs feature" style="left:620px"><span class="feature-ico"><svg width="22" height="22" viewBox="0 0 24 24"><text x="12" y="18" text-anchor="middle" font-size="17" font-weight="700" fill="#fff" font-family="Poppins,sans-serif">$</text></svg></span><div><h4>Transparent Pricing</h4><p>Lorem ipsum dolor sit amet.</p></div></div>
<div class="abs feature" style="left:894px"><span class="feature-ico"><svg width="22" height="22" viewBox="0 0 24 24"><path d="M5 19c0-9 6-14 15-14 0 9-5 15-14 15z" fill="#fff"/></svg></span><div><h4>Eco Friendly</h4><p>Lorem ipsum dolor sit amet.</p></div></div>

<!-- About -->
<div class="abs ghost" style="left:100px;top:1150px">About</div>
<h2 class="abs section-title" style="left:108px;top:1222px">About Us</h2>
<p class="abs about-lead">Lorem ipsum dolor sit amet, consectetur, Ut enim adipiscing elit,sed do eiusmod tempor.</p>
<p class="abs about-copy">Sed ut perspiciatis unde omnis iste natus error sit voluptatem accusantium doloremque laudantium, totam rem aperiam, eaque ipsa quae ab illo inventore veritatis et quasi architecto beatae vitae dicta sunt explicabo. Nemo enim ipsam voluptatem quia voluptas sit aspernatur aut odit aut fugit, sed quia consequuntur magni dolores eos qui ratione voluptatem sequi nesciunt.</p>
<div class="btn btn-grad about-btn">Read More</div>
<div class="photo about-photo" role="img" aria-label="Cleaner vacuuming an office floor"></div>
<div class="abs about-frame"></div>

<!-- Services -->
<div class="abs ghost" style="left:0;width:1200px;text-align:center;top:1808px">Services</div>
<h2 class="abs section-title" style="left:0;width:1200px;text-align:center;top:1886px">Our Services</h2>
<div class="abs card" style="left:72px;width:340px"><div class="photo" style="background:linear-gradient(135deg,#e9e3d6,#b8a98e)" role="img" aria-label="Cleaner wiping a kitchen counter"></div><h3>Service 1</h3><p>Lorem ipsum dolor sit amet, consectetur adipiscing elit, sed do eiusmod tempor incididunt ut labore et dolore magna aliqua.</p><div class="btn btn-grey">Read More</div></div>
<div class="abs card" style="left:430px;width:330px"><div class="photo" style="background:linear-gradient(135deg,#9fc4d8,#4d6f82)" role="img" aria-label="Cleaner washing a window"></div><h3>Service 2</h3><p>Lorem ipsum dolor sit amet, consectetur adipiscing elit, sed do eiusmod tempor incididunt ut labore et dolore magna aliqua.</p><div class="btn btn-grey">Read More</div></div>
<div class="abs card" style="left:788px;width:340px"><div class="photo" style="background:linear-gradient(135deg,#cdd6dc,#7b8792)" role="img" aria-label="Cleaner with a floor machine in a hallway"></div><h3>Service 3</h3><p>Lorem ipsum dolor sit amet, consectetur adipiscing elit, sed do eiusmod tempor incididunt ut labore et dolore magna aliqua.</p><div class="btn btn-grey">Read More</div></div>
<div class="btn btn-grad services-btn">View All Services</div>

<!-- Welcome -->
<div class="abs welcome"></div>
<div class="abs welcome-circle"></div>
<div class="photo welcome-photo" role="img" aria-label="Masked cleaner spraying and wiping a surface"></div>
<p class="abs welcome-kicker">Welcome to</p>
<h2 class="abs welcome-title">Harbor<br>Tidy<br>Squad</h2>
<p class="abs welcome-copy">Lorem ipsum dolor sit amet, consectetur adipiscing elit, sed do eiusmod tempor incididunt ut labore et dolore magna aliqua.</p>
<div class="btn welcome-btn">Contact Us</div>

<!-- Testimonials -->
<div class="abs ghost" style="left:0;width:1200px;text-align:center;top:3400px">Testimonials</div>
<h2 class="abs section-title" style="left:0;width:1200px;text-align:center;top:3452px">Our Testimonials</h2>
<svg class="abs quote-mark" width="96" height="80" viewBox="0 0 96 80"><path d="M4 76V44C4 20 16 6 40 2v14C28 20 22 28 22 40h18v36zM56 76V44C56 20 68 6 92 2v14C80 20 74 28 74 40h18v36z" fill="#f05a22"/></svg>
<p class="abs quote-text">Lorem ipsum dolor sit amet, consectetur adipiscing elit, sed do eiusmod tempor incididunt ut labore et dolore magna aliqua. Ut enim ad minim veniam, quis nostrud exercitation ullamco laboris .</p>
<p class="abs quote-name">Marla Quinlan</p>
<div class="abs stars">
<svg width="20" height="20" viewBox="0 0 24 24"><path d="M12 2l3 7h7l-5.6 4.3 2.1 7.2L12 16l-6.5 4.5 2.1-7.2L2 9h7z" fill="#f7941d"/></svg>
<svg width="20" height="20" viewBox="0 0 24 24"><path d="M12 2l3 7h7l-5.6 4.3 2.1 7.2L12 16l-6.5 4.5 2.1-7.2L2 9h7z" fill="#f7941d"/></svg>
<svg width="20" height="20" viewBox="0 0 24 24"><path d="M12 2l3 7h7l-5.6 4.3 2.1 7.2L12 16l-6.5 4.5 2.1-7.2L2 9h7z" fill="#f7941d"/></svg>
<svg width="20" height="20" viewBox="0 0 24 24"><path d="M12 2l3 7h7l-5.6 4.3 2.1 7.2L12 16l-6.5 4.5 2.1-7.2L2 9h7z" fill="#f7941d"/></svg>
<svg width="20" height="20" viewBox="0 0 24 24"><path d="M12 2l3 7h7l-5.6 4.3 2.1 7.2L12 16l-6.5 4.5 2.1-7.2L2 9h7z" fill="#f7941d"/></svg>
</div>
<div class="abs arrow" style="left:132px"><svg width="16" height="16" viewBox="0 0 24 24"><path d="M15 4l-8 8 8 8" stroke="#fff" stroke-width="3" fill="none"/></svg></div>
<div class="abs arrow" style="left:1022px"><svg width="16" height="16" viewBox="0 0 24 24"><path d="M9 4l8 8-8 8" stroke="#fff" stroke-width="3" fill="none"/></svg></div>

<!-- Contact -->
<div class="abs ghost" style="left:66px;top:3956px">Contact</div>
<h2 class="abs section-title" style="left:70px;top:4030px">Contact Us</h2>
<p class="abs contact-intro">For more information Please fill out the following and we will be in touch shortly</p>
<div class="field" style="left:70px;top:4156px;width:260px">First Name</div>
<div class="field" style="left:350px;top:4156px;width:264px">Second Name</div>
<div class="field" style="left:70px;top:4236px;width:260px">Phone</div>
<div class="field" style="left:350px;top:4236px;width:264px">Subject</div>
<div class="field" style="left:70px;top:4316px;width:544px;height:112px">Message</div>
<div class="btn btn-grad contact-btn">Submit a Message</div>
<div class="photo contact-photo" role="img" aria-label="Cleaner holding a spray bottle and cloth"></div>

<!-- Footer -->
<div class="abs footer" role="img" aria-label="Warm yellow to red backdrop with a faint cleaning photo"></div>
<div class="abs foot-brand"><span class="brand-dot"></span><span class="brand-name">Harbor Tidy<br>Squad</span></div>
<div class="abs socials"><span></span><span></span><span></span></div>
<h3 class="abs foot-head" style="left:550px;top:4708px">Links</h3>
<ul class="abs foot-links"><li>About Us</li><li>Our Services</li><li>Testimonials</li><li>Contact</li></ul>
<h3 class="abs foot-head" style="left:820px;top:4708px">Contact</h3>
<div class="abs foot-contact" style="top:4770px"><span class="ic"><svg width="16" height="16" viewBox="0 0 24 24"><path d="M12 2a7 7 0 0 0-7 7c0 5 7 13 7 13s7-8 7-13a7 7 0 0 0-7-7zm0 9.5A2.5 2.5 0 1 1 12 6a2.5 2.5 0 0 1 0 5.5z" fill="#f05a22"/></svg></span><span>Lorem ipsum lorem ipsum lorem ipsum</span></div>
<div class="abs foot-contact" style="top:4836px"><span class="ic"><svg width="16" height="16" viewBox="0 0 24 24"><path fill="#f05a22" d="M6.6 10.8a15 15 0 0 0 6.6 6.6l2.2-2.2c.3-.3.7-.4 1-.2 1.1.4 2.3.6 3.6.6.6 0 1 .4 1 1V20c0 .6-.4 1-1 1A17 17 0 0 1 3 4c0-.6.4-1 1-1h3.5c.6 0 1 .4 1 1 0 1.3.2 2.5.6 3.6.1.3 0 .7-.2 1z"/></svg></span><span>555-014-2290</span></div>
<div class="abs foot-contact" style="top:4890px"><span class="ic"><svg width="16" height="16" viewBox="0 0 24 24"><rect x="3" y="5" width="18" height="14" rx="2" fill="#f05a22"/><path d="M3 7l9 6 9-6" stroke="#fff" stroke-width="1.6" fill="none"/></svg></span><span>hello@harbortidysquad.com</span></div>
<p class="abs copyright">Copyright © 2020 All Rights Reserved By Harbor Tidy Squad</p>

</body>
</html>
```